Flyer für Weingut
Zielgruppe
Wir sind das Familien Weingut Kolbe aus der Südpalz und wohnen direkt in der Holunderstraße. Eine Straße die viele Touristen anzieht. Wir möchten dieses Jahr das erste mal einen art Gutsauschank eröffnen. Indem es kleinigkeiten zu Essen und unseren Wein zu trinken gibt. Wir möchten sowohl die Touristen einfangen aber auch vorallem einheimische aus den nachbar Orten als Kunden gewinnen. Jeder ist willkomen von jung bis alt.
Aufgabenstellung
modern, ansprechend, professionell, klar, strukuriert, besonders.
Öffnungszeiten unseres Ausschanks: Mittwoch bis Sonntag ab 22.08.25 bis 02.11.25 von 14-20 Uhr
Es gibts kleinigkeiten zu essen zum beispiel Flammkuchen, Pfälzer Tapas oder auch Gemische Wurst/Käse Platten. Getränke: Offene Weine oder Flaschenweine, Weinschorle. Die Essensauswahl soll nicht genaustens aufgelistet werden. Es reicht zum Beispiel: Kleinigkeiten zum Essen oder ähnliches.
Zusatzinfos: Kleiner Hof mit Gartenmöbel. Platz für ca. 50 Leute. Kleine Louge Ecke mit Loungemöbeln. Es gibt nur Selbstbedienung. Gemütliche, lockere Atmosphäre. Vielfältige Weinauswahl.
Wir möchten speziell von Mischgetränken Abstand nehmen. Wir als Familienweingut stehen hinter unserem Produkt und möchten vorallem auch den jungen Leuten den Wein wieder näher bringen. Wir haben Ihnen unten auch ein paar Beispiele hochgeladen in welche Richtung es gehen könnte.
Wichtrig ist das auf unserem Flyer die Kontakdaten, Adresse sowie Instagramname zu finden sind. Nicht sehr groß unjd presänt am besten in einer Ecke.
Unser Logo sollte zu sehen sein. Muss aber nicht unbedingt in den Vordergrund. Die Zeiten sowie Essen und Getränke. Oder anstatt die Getränke gleich eine passende Überschrift wie Gutsauschank oder ähnliches. Auch ein entworfenes Logo wie unten in den Beispielen könnten wir uns vorstellen.
Der flyer allgemein sollte nicht all zu viel Text haben.

```html
<!DOCTYPE html>
<html lang="de">
<head>
<meta charset="utf-8">
<title>Gutsausschank Kolbe – Flyer</title>
<link rel="stylesheet" href="https://fonts.googleapis.com/css2?family=Bagel+Fat+One&family=Oswald:wght@400;500&family=Playfair+Display:wght@700&display=swap">
<style>
  :root {
    --canvas: #ecebe8;
    --cream: #efe6cf;
    --text-light: #ece6d8;
    --text-soft: rgba(236, 230, 216, 0.82);
    --sky-top: #5b5c5a;
    --sky-mid: #4a4d45;
    --vine-dark: #2c3020;
    --soil: #3a2c1e;
    --frame-line: rgba(240, 232, 215, 0.75);
  }
  * { margin: 0; padding: 0; box-sizing: border-box; }
  html, body { width: 1200px; height: 846px; overflow: hidden; background: var(--canvas); }

  .flyer {
    position: absolute;
    left: 318px; top: 23px;
    width: 564px; height: 800px;
    overflow: hidden;
  }
  .flyer__backdrop {
    position: absolute; inset: 0;
    background:
      linear-gradient(180deg, rgba(85,86,84,0.95) 0%, rgba(74,77,69,0.75) 28%, rgba(0,0,0,0) 50%),
      linear-gradient(180deg, var(--sky-top) 0%, var(--sky-mid) 35%, var(--vine-dark) 65%, var(--soil) 100%);
  }

  .brand {
    position: absolute; top: 12px; left: 50%; transform: translateX(-50%);
    display: flex; align-items: center; gap: 8px;
    font-family: "Oswald", sans-serif; font-weight: 500;
    font-size: 26px; letter-spacing: 3px; color: var(--text-light);
  }
  .brand__dot { width: 10px; height: 10px; background: var(--text-light); }

  .presents {
    position: absolute; top: 60px; width: 100%; text-align: center;
    font-family: "Oswald", sans-serif; font-weight: 500;
    font-size: 13px; letter-spacing: 1px; color: var(--text-light);
  }

  .headline {
    position: absolute; top: 82px; width: 100%; text-align: center;
    font-family: "Bagel Fat One", sans-serif; font-weight: 400;
    color: var(--cream); line-height: 58px; letter-spacing: 1px;
    text-transform: uppercase;
  }
  .headline__line { display: block; font-size: 50px; }

  .intro {
    position: absolute; top: 206px; width: 100%; text-align: center;
    font-family: "Oswald", sans-serif; font-weight: 400;
    font-size: 11.5px; line-height: 15px; letter-spacing: 0.4px;
    color: var(--text-light); text-transform: uppercase;
  }

  .arch-frame { position: absolute; left: 0; top: 0; }
  .arch-photo {
    position: absolute; left: 164px; top: 279px; width: 245px; height: 411px;
    border-radius: 122px 122px 0 0;
    background: linear-gradient(180deg, #f3ead6 0%, #d9c59a 25%, #7d8a4a 55%, #4f5f3a 80%, #b39a5e 100%);
  }

  .info {
    position: absolute; width: 130px; text-align: center;
    font-family: "Playfair Display", serif; font-weight: 700;
    font-size: 15px; line-height: 20px; letter-spacing: 1px;
    color: var(--text-light); text-transform: uppercase;
  }
  .info--dates { left: 12px; top: 392px; }
  .info--hours { left: 432px; top: 388px; }

  .tagline {
    position: absolute; top: 716px; width: 100%; text-align: center;
    font-family: "Bagel Fat One", sans-serif; font-weight: 400;
    font-size: 27px; line-height: 34px; letter-spacing: 1px;
    color: var(--cream); text-transform: uppercase;
  }

  .offer {
    position: absolute; top: 752px; width: 100%; text-align: center;
    font-family: "Oswald", sans-serif; font-weight: 400;
    font-size: 11px; line-height: 14px; letter-spacing: 0.8px;
    color: var(--text-light); text-transform: uppercase;
  }

  .contact {
    position: absolute; bottom: 8px;
    font-family: "Oswald", sans-serif; font-weight: 400;
    font-size: 9.5px; line-height: 12px; letter-spacing: 0.4px;
    color: var(--text-soft);
  }
  .contact--address { left: 14px; text-align: left; }
  .contact--social { right: 14px; text-align: right; }
</style>
</head>
<body>
  <main class="flyer">
    <div class="flyer__backdrop" role="img" aria-label="Foto eines Weinbergs in der Südpfalz bei Abendlicht, oben abgedunkelt"></div>

    <div class="brand"><span class="brand__dot"></span>KOLBE</div>
    <p class="presents">PRÄSENTIERT:</p>

    <h1 class="headline">
      <span class="headline__line">Gutsauschank</span>
      <span class="headline__line">Kolbe</span>
    </h1>

    <p class="intro">
      In der Südpfalz daheim – mit Liebe zum Wein<br>
      Ohne Mischgetränke, ohne Show – nur ehrlicher Genuss.<br>
      Selbstbedienung. Kein Schnickschnack. Einfach gut.
    </p>

    <svg class="arch-frame" width="564" height="800" viewBox="0 0 564 800" aria-hidden="true">
      <path d="M144 711 V403 A142 142 0 0 1 428 403 V711 Z" fill="none" stroke="var(--frame-line)" stroke-width="1.2"/>
    </svg>
    <div class="arch-photo" role="img" aria-label="Foto eines Paares, das im sonnigen Weinberg mit Weingläsern anstößt"></div>

    <p class="info info--dates">Ab 22.<br>August<br>bis 2.<br>November<br>2025</p>
    <p class="info info--hours">Mittwoch<br>bis<br>Sonntag |<br>14 — 20<br>Uhr</p>

    <p class="tagline">Wein. Hof. Sommerfeeling.</p>
    <p class="offer">Offene Weine · Flaschenweine · Kleinigkeiten zum Essen</p>

    <address class="contact contact--address">
      Weingut Kolbe · Holunderstraße 12 · 76829 Rebhausen<br>
      Tel. 06341 555 210
    </address>
    <p class="contact contact--social">Instagram<br>@weingut.kolbe</p>
  </main>
</body>
</html>
```